Award-winnning Estate Agent needs a premium version of their 'For Sale' board design

We need a premium option for our 'For Sale' board design. We have a standard board that is attached to this brief, but were are looking to have a premium design version that we will use when selling exclusive properties. Our company name is Harbour Lane Estates and the name for this is exclusive selection is: 'The Harbour Collection'. The design needs to work with our current brand, but have a distinctive PREMIUM feel to it. I have uploaded the barnd guidelines and also some of the exisisting logo variations. We do NOT need a new logo but feel free to play around with colours, fonts, sizes etc. for the sign.

Target Market(s)

Property buyers & house hunters

Industry/Entity Type

Real Estate - Residential Property

Font styles to use
Sans Serif

Requirements
Must have
• A premium fee, must be square design, must be easy to read when driving past the sign
Nice to have
• I'm open ot ideas

```html
<!DOCTYPE html>
<html lang="en">
<head>
<meta charset="utf-8">
<title>Harbour Lane Estates – For Sale Boards</title>
<link rel="stylesheet" href="https://fonts.googleapis.com/css2?family=Montserrat:wght@500;600&family=Open+Sans:wght@400;600&family=Playfair+Display:ital,wght@1,700&display=swap">
<style>
  :root {
    --page: #ffffff;
    --white: #ffffff;
    --navy: #2b2d86;
    --sky: #1f8fdb;
    --sky-light: #2ea3e3;
    --gold-light: #e6cf93;
    --gold: #c6a560;
    --gold-dark: #8e6c2c;
    --night: #0b0b0b;
    --indigo: #2a2a8c;
    --ocean: #166fb5;
  }
  * { box-sizing: border-box; margin: 0; padding: 0; }
  html, body { width: 1200px; height: 2667px; overflow: hidden; background: var(--page); }
  body { position: relative; font-family: "Open Sans", sans-serif; }

  .board {
    position: absolute;
    left: 248px;
    width: 717px;
    height: 717px;
    background: var(--white);
    box-shadow: 0 6px 14px rgba(0,0,0,0.35);
    overflow: hidden;
  }
  .board--black { top: 107px; }
  .board--indigo { top: 938px; }
  .board--ocean { top: 1772px; }

  .board__scene { position: absolute; left: 0; top: 0; width: 717px; height: 440px; }
  .board--black .board__scene { background: radial-gradient(ellipse at 60% 45%, #262626 0%, var(--night) 75%); }
  .board--indigo .board__scene { background: radial-gradient(ellipse at 55% 40%, #3a3aa6 0%, var(--indigo) 75%); }
  .board--ocean .board__scene { background: radial-gradient(ellipse at 40% 50%, #2286d0 0%, var(--ocean) 55%, #0f5b98 100%); }

  .board__stripe { position: absolute; left: 0; top: 437px; width: 717px; height: 11px; }
  .board--black .board__stripe { background: var(--sky); }
  .board--indigo .board__stripe { background: var(--sky-light); }
  .board--ocean .board__stripe { background: var(--navy); border-bottom: 3px solid var(--white); }

  .board__for {
    position: absolute; left: 0; top: 66px; width: 670px; text-align: center;
    font-family: "Montserrat", sans-serif; font-weight: 600; font-size: 124px; line-height: 1;
    color: var(--white); letter-spacing: -2px;
  }
  .board__sale {
    position: absolute; left: 166px; top: 96px;
    font-family: "Playfair Display", serif; font-style: italic; font-weight: 700;
    font-size: 250px; line-height: 1; letter-spacing: -8px;
    background: linear-gradient(100deg, var(--gold-dark) 0%, var(--gold) 30%, var(--gold-light) 55%, var(--gold) 75%, var(--gold-dark) 100%);
    -webkit-background-clip: text; background-clip: text; color: transparent;
  }
  .board__web {
    position: absolute; left: 0; top: 328px; width: 717px; text-align: center;
    font-size: 30px; color: var(--white); letter-spacing: 0.2px;
  }

  .board__phone {
    position: absolute; left: 124px; top: 406px; width: 480px; height: 77px;
    border-radius: 22px;
    background: linear-gradient(100deg, var(--gold-dark) 0%, var(--gold) 25%, var(--gold-light) 50%, var(--gold) 75%, var(--gold-dark) 100%);
    display: flex; align-items: center; justify-content: center;
    font-family: "Montserrat", sans-serif; font-weight: 500; font-size: 58px; color: var(--white);
    letter-spacing: -1px; text-shadow: 0 2px 3px rgba(0,0,0,0.45);
  }
  .board__phone-shadow {
    position: absolute; left: 160px; top: 482px; width: 410px; height: 16px;
    background: radial-gradient(ellipse at 50% 0%, rgba(0,0,0,0.28) 0%, rgba(0,0,0,0) 70%);
  }

  .brand { position: absolute; left: 86px; top: 500px; height: 130px; display: flex; align-items: center; }
  .brand__mark { width: 150px; height: 118px; background: var(--sky); }
  .brand__divider { width: 2px; height: 118px; background: #bcd6ee; margin-left: 34px; }
  .brand__name {
    margin-left: 16px; font-family: "Open Sans", sans-serif; font-weight: 600;
    font-size: 31px; color: var(--navy); white-space: nowrap;
  }

  .board__base { position: absolute; left: 0; top: 675px; width: 717px; height: 13px; }
  .board--black .board__base, .board--ocean .board__base { background: var(--navy); }
  .board--indigo .board__base { background: var(--sky-light); }
</style>
</head>
<body>

<section class="board board--black">
  <div class="board__scene" role="img" aria-label="Dimmed photograph of a furnished living room"></div>
  <div class="board__stripe"></div>
  <div class="board__for">FOR</div>
  <div class="board__sale">sale</div>
  <div class="board__web">www.harbourlaneestates.co.uk</div>
  <div class="board__phone-shadow"></div>
  <div class="board__phone">01632 960142</div>
  <div class="brand">
    <div class="brand__mark"></div>
    <div class="brand__divider"></div>
    <div class="brand__name">Harbour Lane Estates</div>
  </div>
  <div class="board__base"></div>
</section>

<section class="board board--indigo">
  <div class="board__scene" role="img" aria-label="Indigo tinted photograph of a furnished living room"></div>
  <div class="board__stripe"></div>
  <div class="board__for">FOR</div>
  <div class="board__sale">sale</div>
  <div class="board__web">www.harbourlaneestates.co.uk</div>
  <div class="board__phone-shadow"></div>
  <div class="board__phone">01632 960142</div>
  <div class="brand">
    <div class="brand__mark"></div>
    <div class="brand__divider"></div>
    <div class="brand__name">Harbour Lane Estates</div>
  </div>
  <div class="board__base"></div>
</section>

<section class="board board--ocean">
  <div class="board__scene" role="img" aria-label="Blue tinted photograph of a furnished living room"></div>
  <div class="board__stripe"></div>
  <div class="board__for">FOR</div>
  <div class="board__sale">sale</div>
  <div class="board__web">www.harbourlaneestates.co.uk</div>
  <div class="board__phone-shadow"></div>
  <div class="board__phone">01632 960142</div>
  <div class="brand">
    <div class="brand__mark"></div>
    <div class="brand__divider"></div>
    <div class="brand__name">Harbour Lane Estates</div>
  </div>
  <div class="board__base"></div>
</section>

</body>
</html>
```